Need Bold and Innovative Book Cover

Hi,

I am in need of a bold and innovative book cover to catch the attention of people.

Here is what the book is about:

Title: Quiet Harvest - Taming Clutter To Build Your Calmest Season Yet

Author: Captain Dale Farrow

This book is about how to eliminate overwhelm, stress, and information overload from your life. This book is a guide to teach people how I made my life better by getting rid of all kinds of stress, overwhelm, etc.

I have an information product that we created the book from. You can watch the video here to have an even better idea.

http://quietharvestbook.example/

In addition here is an instructional video about what I would like to see for the cover.

http://clipvault.example/t/QpRtZkLmWvA

I look forward to the designs.

Thanks!
Updates

Project Deadline Extended
Reason: Several designers needed a bit more time.

Project Deadline Extended
Reason: Need more time to work on this. Dale

Target Market(s)

Busy people who want to get more done.

Industry/Entity Type

Product

Requirements
Must have
• Model the info product so it all ties in but also use your own creativity.

```html
<!DOCTYPE html>
<html lang="en">
<head>
<meta charset="utf-8">
<title>Quiet Harvest – Book Cover</title>
<link rel="stylesheet" href="https://fonts.googleapis.com/css2?family=Josefin+Slab:wght@300&family=Arvo:wght@400;700&display=swap">
<style>
  :root {
    --page: #ffffff;
    --cover-top: #ffffff;
    --cover-bottom: #d9d9d9;
    --ink: #111111;
    --ink-soft: #2a2a2a;
    --photo-light: #bdbdbd;
    --photo-mid: #5a5a5a;
    --photo-dark: #0b0b0b;
    --dot: #ffffff;
  }
  * { margin: 0; padding: 0; box-sizing: border-box; }
  html, body {
    width: 1200px; height: 1000px; overflow: hidden;
    background: var(--page);
  }
  .canvas {
    position: relative; width: 1200px; height: 1000px;
    display: flex; align-items: center; justify-content: center;
  }
  .book-cover {
    position: relative; width: 600px; height: 900px; overflow: hidden;
    background: linear-gradient(180deg, var(--cover-top) 0%, #f1f1f1 40%, var(--cover-bottom) 100%);
    color: var(--ink);
  }
  .title-block { position: absolute; left: 32px; top: 40px; }
  .book-title {
    font-family: "Josefin Slab", serif; font-weight: 300;
    font-size: 96px; line-height: 0.86; color: var(--ink-soft);
    letter-spacing: 1px;
  }
  .book-subtitle {
    margin-top: 14px;
    font-family: "Arvo", serif; font-weight: 400;
    font-size: 26px; line-height: 1.05;
    font-variant: small-caps; letter-spacing: 3px; color: var(--ink-soft);
  }
  .book-author {
    margin-top: 8px;
    font-family: "Arvo", serif; font-weight: 700; font-size: 21px;
  }
  .teaser {
    position: absolute; left: 372px; top: 345px; width: 200px;
    font-family: "Arvo", serif; font-weight: 700;
  }
  .teaser-lead { font-size: 44px; line-height: 0.9; }
  .teaser-body { font-size: 18px; line-height: 1.12; }
  .cover-photo {
    position: absolute; left: 0; bottom: 0; width: 600px; height: 390px;
    background:
      radial-gradient(ellipse 70% 60% at 45% 35%, var(--photo-mid) 0%, var(--photo-dark) 70%),
      var(--photo-dark);
    -webkit-mask-image: linear-gradient(180deg, transparent 0%, #000 18%);
            mask-image: linear-gradient(180deg, transparent 0%, #000 18%);
  }
  .question-mark { position: absolute; left: 90px; top: 360px; width: 200px; height: 280px; }
</style>
</head>
<body>
  <main class="canvas">
    <article class="book-cover">
      <header class="title-block">
        <h1 class="book-title">Quiet<br>Harvest</h1>
        <p class="book-subtitle">Taming Clutter To Build<br>Your Calmest Season Yet</p>
        <p class="book-author">by Captain Dale Farrow</p>
      </header>

      <div class="cover-photo" role="img" aria-label="Black and white photograph of a man's bowed shaved head held in his hands, seen from above"></div>

      <svg class="question-mark" viewBox="0 0 200 280" aria-hidden="true">
        <path d="M18 70 C18 25 55 5 98 5 C150 5 182 35 182 78 C182 118 150 135 124 150 C108 160 104 170 104 195 L68 195 C68 160 76 140 104 124 C128 110 140 100 140 80 C140 56 122 42 98 42 C72 42 58 58 58 82 Z" fill="var(--ink)"/>
        <circle cx="86" cy="240" r="22" fill="var(--dot)"/>
      </svg>

      <section class="teaser">
        <p class="teaser-lead">how</p>
        <p class="teaser-body">to eliminate<br>overwhelm,<br>stress, and<br>information<br>overload from<br>your life.</p>
      </section>
    </article>
  </main>
</body>
</html>
```